Wordpress Design Project

I now need a Wordpress theme for my new business.
The business offers consultancy on Information Management, Knowledge Management, Records Management and Document Management.
The winning designer must be able to set up the site for me on my webspace provided by Kestrowave Hosting, or talk me through how to do this.
I already have a logo designed which you can see by viewing my profile on here. I am happy to send copies of the original artwork to bidders.
I recently sold my interest in a very similar business, and want a website similar to (but not the same as) the previous company (who are now my competition!) This website can be viewed at www.trulvanworks.example
Categories will be similar, but I would like everything to be as configurable as possible.
I have a strong preference for clean unfussy design.
I want original design please. Please no templates from free to use sites with stock images... no jigsaw pictures!!!!
Love this one... http://www.quellimar.example/
Please get in touch with any questions.
Reason: All of these are too generic (brief says no jigsaw puzzle images), or have copied HPS which is the COMPETITION - so I don't want the site to look like theirs
Reason: Please keep trying people
Business
Business

```html
<!DOCTYPE html>
<html lang="en">
<head>
<meta charset="utf-8">
<title>Harrowfield Professional Services</title>
<link rel="stylesheet" href="https://fonts.googleapis.com/css2?family=Arimo:wght@700&family=Gelasio:ital,wght@0,400;1,400&display=swap">
<style>
:root{
  --navy:#1f2d6b;
  --blue:#2a86cc;
  --header-top:#cfe2f2;
  --header-mid:#5f96cc;
  --header-bot:#2f68ad;
  --hero-light:#e4e4e4;
  --hero-dark:#9c9c9c;
  --ink:#5a5a5a;
  --muted:#777;
  --footer-bg:#ececec;
  --bar-bg:#f6f7f9;
  --button:#6a8bb6;
  --deep:#1d4f8c;
  --dot:#2a5f9e;
}
*{margin:0;padding:0;box-sizing:border-box}
html,body{width:901px;height:1200px;overflow:hidden;background:#fff}
body{position:relative;font-family:'Gelasio',Georgia,serif;color:var(--ink)}
.abs{position:absolute}

/* header */
.site-header{left:0;top:0;width:901px;height:185px;
  background:linear-gradient(180deg,var(--header-top) 0%,var(--header-mid) 55%,var(--header-bot) 100%)}
.brand-name{left:300px;top:38px;width:301px;text-align:center;font-size:37px;letter-spacing:1px;color:var(--navy);line-height:1}
.brand-sub{left:300px;top:87px;width:301px;text-align:center;font-size:12px;letter-spacing:4.6px;color:var(--navy);line-height:1}
.header-rule{left:60px;top:134px;width:780px;height:1px;background:rgba(255,255,255,.35)}
.main-nav a{position:absolute;top:146px;font-style:italic;font-size:19px;color:#fff;text-decoration:none;
  text-shadow:0 1px 2px rgba(0,0,0,.45);white-space:nowrap}

/* hero */
.hero{left:0;top:185px;width:901px;height:388px;
  background:radial-gradient(ellipse at 65% 40%,var(--hero-light),var(--hero-dark) 110%);
  border-top:2px solid #8a8a8a}
.hero-map{left:420px;top:40px;width:470px;height:300px;
  background:radial-gradient(ellipse,rgba(255,255,255,.4),rgba(255,255,255,0) 70%)}
.hero-figure{left:70px;top:25px;width:380px;height:345px;
  background:linear-gradient(180deg,rgba(150,140,135,.45) 0%,rgba(120,130,150,.45) 45%,rgba(40,90,160,.55) 80%,rgba(160,160,160,0) 100%)}
.hero-line{font-style:italic;color:#2a2a2a;white-space:nowrap;line-height:1}
.slider-dots{left:723px;top:538px;display:flex;gap:7px}
.slider-dots span{width:23px;height:23px;border-radius:50%;background:var(--dot)}
.slider-dots span.active{background:#e8e8e8}

/* content */
.service-photo{width:161px;height:158px;border:4px solid #d8d8d8;
  background:linear-gradient(135deg,#e9e9e9,#b5b0a8 60%,#7b7571)}
.service-title{font-family:'Arimo',Arial,sans-serif;font-weight:700;font-size:14px;color:var(--navy);white-space:nowrap}
.service-text{width:505px;font-style:italic;font-size:10px;line-height:14px;color:var(--ink)}
.service-text p+p{margin-top:7px}
.search-btn{width:62px;height:62px;border-radius:50%;background:var(--button);
  box-shadow:0 0 0 3px #cfdcec}
.search-btn svg{position:absolute;left:20px;top:20px}
.divider{left:52px;top:773px;width:790px;height:1px;background:linear-gradient(90deg,transparent,#a9bcd3 30%,#a9bcd3 70%,transparent)}
.scroll-track{left:841px;top:599px;width:1px;height:365px;background:#777}
.scroll-thumb{left:838px;top:618px;width:7px;height:24px;border-radius:3px;background:var(--deep)}

/* footer */
.hatch{left:0;top:980px;width:901px;height:11px;
  background:repeating-linear-gradient(135deg,#d6d6d6 0 1px,#f4f4f4 1px 3px)}
.footer-bar{left:0;top:991px;width:901px;height:27px;background:var(--bar-bg);border-top:1px solid #b9c8db}
.footer-nav{left:49px;top:1000px;font-style:italic;font-size:10px;color:var(--muted);white-space:nowrap}
.footer-nav a{color:var(--muted);text-decoration:none}
.footer-nav a.current{color:var(--blue)}
.footer-nav i{margin:0 9px;color:#bbb}
.copyright{left:610px;top:1000px;font-style:italic;font-size:10px;color:#8aa3c2}
.footer-main{left:0;top:1018px;width:901px;height:182px;background:var(--footer-bg)}
.col-heading{font-family:'Arimo',Arial,sans-serif;font-weight:700;font-size:16.5px;line-height:19px;color:var(--navy)}
.col-heading span{color:var(--blue)}
.col-text{font-style:italic;font-size:9.5px;line-height:18px;color:var(--muted)}
.story-rule{left:49px;top:1118px;width:210px;height:1px;background:#d0d0d0}
.email-field{left:292px;top:1131px;width:207px;height:27px;background:var(--deep);border:2px solid #9bb6d6;
  font-style:italic;font-size:10.5px;color:#a8c0dc;padding:5px 10px}
.email-tail{left:438px;top:1156px}
.signup{left:452px;top:1160px;font-style:italic;font-size:12px;color:var(--blue)}
.contact-text{left:528px;top:1058px;width:320px;font-style:italic;font-size:9.2px;line-height:19px;color:var(--muted);white-space:nowrap}
.news-box{left:531px;top:1131px;width:307px;height:42px;background:linear-gradient(180deg,#1f5fa8,#163f78);
  border:2px solid #9bb6d6;font-family:'Arimo',Arial,sans-serif;font-weight:700;font-size:16px;color:#fff;padding:10px 17px}
.news-box span{color:#7ec0ee}
</style>
</head>
<body>

<header class="abs site-header">
  <div class="abs brand-name">HARROWFIELD</div>
  <div class="abs brand-sub">PROFESSIONAL SERVICES</div>
  <div class="abs header-rule"></div>
  <nav class="main-nav">
    <a style="left:57px">Home</a>
    <a style="left:176px">About HPS</a>
    <a style="left:338px">News</a>
    <a style="left:452px">Technology</a>
    <a style="left:618px">Services</a>
    <a style="left:756px">Contct us</a>
  </nav>
</header>

<section class="abs hero">
  <div class="abs hero-map" role="img" aria-label="Faint world map behind the headline"></div>
  <div class="abs hero-figure" role="img" aria-label="Group of business people standing behind a rising blue arrow"></div>
  <div class="abs hero-line" style="left:362px;top:33px;font-size:28.5px">Enterprise Information Governance</div>
  <div class="abs hero-line" style="left:455px;top:97px;font-size:33px">Business and Technology</div>
  <div class="abs hero-line" style="left:463px;top:166px;font-size:33px">Consulting Group</div>
</section>
<div class="abs slider-dots"><span class="active"></span><span></span><span></span><span></span></div>

<main>
  <article>
    <div class="abs service-photo" style="left:52px;top:599px" role="img" aria-label="Consultant presenting at a flip chart to a colleague"></div>
    <h2 class="abs service-title" style="left:233px;top:601px">Records and Information Management</h2>
    <div class="abs service-text" style="left:233px;top:632px">
      <p>Records management is the practice of maintaining the records of an organisation from the time they are created up to their eventual disposal. This may include classifying, storing, securing, and destruction (or in some cases, archival preservation) of records.</p>
      <p>Ineffective record keeping can negatively impact on regulatory compliance, litigation readiness, operational productivity and cost control. By understanding your records, information and business needs HPS’s records management team can help link your hard copy and electronic records to robust policies based on current legislation and your company’s unique business requirements.</p>
    </div>
    <div class="abs search-btn" style="left:753px;top:632px">
      <svg width="22" height="22" viewBox="0 0 22 22"><circle cx="7" cy="7" r="4.5" fill="none" stroke="#fff" stroke-width="2.4"/><line x1="10.5" y1="10.5" x2="17" y2="16" stroke="#fff" stroke-width="3" stroke-linecap="round"/></svg>
    </div>
  </article>
  <div class="abs divider"></div>
  <article>
    <div class="abs service-photo" style="left:52px;top:804px" role="img" aria-label="Two colleagues reviewing a document at a desk"></div>
    <h2 class="abs service-title" style="left:233px;top:806px">Information Governance &amp; Content Management</h2>
    <div class="abs service-text" style="left:233px;top:837px">
      <p>Records management is the practice of maintaining the records of an organisation from the time they are created up to their eventual disposal. This may include classifying, storing, securing, and destruction (or in some cases, archival preservation) of records.</p>
      <p>Ineffective record keeping can negatively impact on regulatory compliance, litigation readiness, operational productivity and cost control. By understanding your records, information and business needs HPS’s records management team can help link your hard copy and electronic records to robust policies based on current legislation and your company’s unique business requirements.</p>
    </div>
    <div class="abs search-btn" style="left:753px;top:838px">
      <svg width="22" height="22" viewBox="0 0 22 22"><circle cx="7" cy="7" r="4.5" fill="none" stroke="#fff" stroke-width="2.4"/><line x1="10.5" y1="10.5" x2="17" y2="16" stroke="#fff" stroke-width="3" stroke-linecap="round"/></svg>
    </div>
  </article>
  <div class="abs scroll-track"></div>
  <div class="abs scroll-thumb"></div>
</main>

<footer>
  <div class="abs hatch"></div>
  <div class="abs footer-bar"></div>
  <nav class="abs footer-nav">
    <a class="current">Home</a><i>/</i><a>About HPS</a><i>/</i><a>News</a><i>/</i><a>Technology</a><i>/</i><a>Services</a><i>/</i><a>Contct us</a>
  </nav>
  <div class="abs copyright">Copyright ©2012</div>
  <div class="abs footer-main"></div>

  <section>
    <h3 class="abs col-heading" style="left:49px;top:1031px">CLIENT<br><span>SUCCESS STORIES</span></h3>
    <p class="abs col-text" style="left:49px;top:1075px;width:215px">HPS Systems help the Corvane Group Improve Compliance with the Data Protection Act</p>
    <div class="abs story-rule"></div>
    <p class="abs col-text" style="left:49px;top:1124px;width:215px">HPS Systems works with the Northvale Air Ambulance (NVAA) to improve Data Protection Compliance</p>
  </section>

  <section>
    <h3 class="abs col-heading" style="left:290px;top:1030px">THE HPS<br><span>NEWSLETTER</span></h3>
    <p class="abs col-text" style="left:290px;top:1073px;width:215px;line-height:17px">Sign up and we’ll keep you notified on any announcements regarding changes to our site or our products &amp; services.</p>
    <div class="abs email-field">Enter your e-mail...</div>
    <svg class="abs email-tail" width="16" height="16" viewBox="0 0 16 16"><path d="M0 0 L16 0 L8 14 Z" fill="#1d4f8c"/></svg>
    <div class="abs signup">Sign Up</div>
  </section>

  <section>
    <h3 class="abs col-heading" style="left:528px;top:1031px;color:var(--blue);font-size:19px">CONTACT</h3>
    <p class="abs contact-text">HPS’s UK offices are centrally located in<br>close proximity to the M40, Oxford and trains.<br>Tel: 01632 960481 &nbsp;/&nbsp; Fax: 01632 960482 &nbsp;/&nbsp; office@harrowfield.example</p>
    <div class="abs news-box">LATEST <span>NEWS</span></div>
  </section>
</footer>

</body>
</html>
```